Personal Business Card Design Project

I am looking for a business card to be able to hand to both Chinese and Australian businessman.
I am a self employed consultant and just need my name, phone number and email address on the card. No Business Name and No Website.
I want it to look like an exclusive prestigious card.
I would like the background to be be a glossy red and the writing to be gold. (This applies to both sides of the card).
It must have English on one side and Chinese (Mandarin) on the reverse.
Details you will require
Name : Derek Hollins
Phone : + 61 428 903 574
Email : derekhollins@mailvanto.com
Updates
Thank you everybody for your designs.
Industry/Entity Type
Business

```html
<!DOCTYPE html>
<html lang="en">
<head>
<meta charset="utf-8">
<title>Derek Hollins – Business Card</title>
<link rel="stylesheet" href="https://fonts.googleapis.com/css2?family=Playball&family=Marcellus&display=swap">
<style>
  :root {
    --card-black: #000000;
    --card-red: #ff0000;
    --card-gold: #ffff00;
    --name-shadow: rgba(60, 0, 0, 0.85);
  }
  html, body {
    margin: 0;
    padding: 0;
    overflow: hidden;
    background: var(--card-black);
  }
  .card {
    position: relative;
    width: 1200px;
    height: 741px;
    background: var(--card-black);
    overflow: hidden;
  }
  .name-panel {
    position: absolute;
    left: 9px;
    top: 9px;
    width: 1182px;
    height: 575px;
    background: var(--card-red);
    display: flex;
    align-items: center;
    justify-content: center;
  }
  .holder-name {
    margin: 0;
    font-family: "Playball", cursive;
    font-weight: 400;
    font-size: 158px;
    line-height: 1;
    color: var(--card-gold);
    text-shadow: 4px 5px 5px var(--name-shadow);
    white-space: nowrap;
    transform: translateY(-6px);
  }
  .contact {
    position: absolute;
    left: 73px;
    top: 603px;
    margin: 0;
    font-family: "Marcellus", serif;
    font-size: 39px;
    line-height: 56px;
    color: var(--card-gold);
    font-style: normal;
  }
  .contact span {
    display: block;
  }
</style>
</head>
<body>
  <main class="card">
    <section class="name-panel">
      <h1 class="holder-name">Derek Hollins</h1>
    </section>
    <address class="contact">
      <span class="contact-phone">+ 61 428 903 574</span>
      <span class="contact-email">derekhollins@mailvanto.com</span>
    </address>
  </main>
</body>
</html>
```